Norma chewable tablets 3 panel sticker/template for tablet line - sticker die line is attached.

Sticker design for our line of chewable THC tablets. Product name is "Chewables" We have 4 flavor varieties of tablets - Matcha Peppermint, Ginger, Lavender Pomegranate, & Lemon Chiffon. Please design the basic peel and reveal label, that will be easy to change just colors and a few details on to designate each formula. see inspiration photo attached.

(B in norma is lower case.) Please also see other product packaging within our line, to coordinate your design with. Thanks! ;-) All compliance fonts must be 1/16th" or larger.

Target Market(s)

21+ professional women and/or men, looking for lower dose THC products - more functional products, to help with sleep, anxiety, pain, inflammation and just relaxing/recharging.

Industry/Entity Type

Cannabis

Font styles to use
Serif
Other font styles liked:
• See attached packaging to match font & coordinate look with.

Requirements
Must have
• This design includes 3 panels, as this is peel and reveal sticker that fits on a small box that slides to open. View box here: https://vantobox.com/packaging/glidecase/

Needs a peel back suggestion, so people know to open the sticker.

All compliance language must be at least 1/16" font size.

Panel 1 is the marketing layer must have the THC logo and the following warning statement "CONTAINS MARIJUANA. KEEP AWAY FROM CHILDREN." This warning statement must be directly below the THC logo - see attachment for THC icon/logo. Icon/THC logo must be 1/2" in size on final sticker and in red, exactly as shown in attachment this font must be 1/16"

Product name: Chewables or Chewables by Norma (perhaps incorporate our logo with the flower?)
SKU specific details: Ginger, 3 mg THC, 10 mg CBD, 3 mg CBG. 30 fast acting chewable tablets.
Please also try to incorporate the pattern that is attached on this panel, that is carried over from our other products in this line. Colors can shift to match flavor. (Note, this packaging does not need the water color design or floral icon additions like other packaging has), the windowpane design is enough carry over.

Since this is such a small surface, let's keep it pretty clean and simple.

This outside panel/marketing layer of the sticker will be silver backed, so feel free to incorporate that to show through in the design if possible.

Middle section panel of the sticker will list ingredients:

Ginger, sugar, maltodextrin, magnesium stearate, microcrystalline cellulose, dicalcium phosphate, silicon dioxide, and food grade colorant, hemp derived CBD and CBG, cannabis derived THC.

Also on this ingredient panel or regulatory language panel, please have a product facts box containing this:

Serving size 1 tablet = 3 mg THC, 10 mg CBD, 3 mg CBG
Total cannabinoids per package 90 mg THC, 300 mg CBD, 90 mg CBG.
480 mg total cannabinoids. Total net weight: 10.5 g

www.normavelta.com
Store in a cool dry place.

(This ingredient panel will change slightly with each SKU, so it needs to be editable as we create new SKUs. panels 2 & 3 can be black and white since it is just text.)

Final panel should be this compliance language:

THIS PRODUCT WAS PRODUCED WITHOUT REGULATORY OVERSIGHT FOR HEALTH, SAFETY, OR EFFICACY. THERE MAY BE LONG TERM PHYSICAL OR MENTAL HEALTH RISKS FOR USE OF MARIJUANA INCLUDING ADDITIONAL RISKS FOR WOMEN WHO ARE OR MAY BE PREGNANT OR ARE BREASTFEEDING. USE OF MARIJUANA MAY IMPAIR YOUR ABILITY TO DRIVE A CAR OR OPERATE MACHINERY. THE INTOXICATING EFFECTS OF THIS PRODUCT MAY BE DELAYED BY UP TO 4 HOURS.
Should not have
• No pot leaves or typical stoner representations.

```html
<!DOCTYPE html>
<html lang="en">
<head>
<meta charset="utf-8">
<title>Chewables by Norma – peel and reveal labels</title>
<link href="https://fonts.googleapis.com/css2?family=Noto+Serif:wght@400&family=Playfair+Display:wght@700&family=Rubik:wght@800&family=Source+Sans+3:wght@400;600;700&display=swap" rel="stylesheet">
<style>
  :root{
    --pink:#c2449a;
    --pink-soft:#c9559f;
    --ink:#111;
    --warn-red:#e0202a;
    --sku-grey:#8a7f86;
    --lemon-a:#f3e97e; --lemon-b:#e8dc4e;
    --ginger-a:#e2e2e2; --ginger-b:#bdbdbd;
    --lavender-a:#dacbe6; --lavender-b:#b9a0d0;
    --matcha-a:#8fd1a8; --matcha-b:#5eaf80;
  }
  *{margin:0;padding:0;box-sizing:border-box}
  html,body{width:1200px;height:960px;overflow:hidden;background:#fff}
  .sheet{position:relative;width:1200px;height:960px}

  .label{position:absolute;width:514px;height:247px;overflow:hidden;--flavor-text:#fff}
  .label--lemon{left:20px;top:17px;background:linear-gradient(110deg,var(--lemon-b),var(--lemon-a) 45%,var(--lemon-b));--flavor-text:#f1e46a}
  .label--ginger{left:666px;top:17px;background:linear-gradient(110deg,var(--ginger-b),var(--ginger-a) 45%,var(--ginger-b));--flavor-text:#ececec}
  .label--lavender{left:20px;top:339px;background:linear-gradient(110deg,var(--lavender-b),var(--lavender-a) 45%,var(--lavender-b));--flavor-text:#dccbe7}
  .label--matcha{left:666px;top:339px;background:linear-gradient(110deg,var(--matcha-b),var(--matcha-a) 45%,var(--matcha-b));--flavor-text:#93d6ab}

  .label__frame{position:absolute;left:9px;top:10px;right:10px;bottom:10px;border:1.3px solid var(--ink);border-radius:18px}
  .peel-tab{position:absolute;right:0;top:0;width:72px;height:62px;background:var(--pink-soft);border-bottom-left-radius:100% 100%}
  .peel-tab svg{position:absolute;right:14px;top:12px}

  .thc-icon{position:absolute;left:45px;top:42px}
  .warning{position:absolute;left:0;width:188px;top:168px;text-align:center;font:700 12px/16.5px "Source Sans 3",sans-serif;color:var(--ink)}
  .divider{position:absolute;left:188px;top:37px;width:2px;height:178px;background:var(--pink)}

  .brand{position:absolute;left:206px;top:44px}
  .brand__line{font:400 18px/1 "Noto Serif",serif;letter-spacing:4px;color:var(--ink);margin-left:24px}
  .brand__name{display:flex;align-items:center;gap:8px;margin-top:-8px}
  .brand__word{font:700 72px/1 "Playfair Display",serif;color:var(--pink)}
  .brand__dot{width:26px;height:26px;border-radius:50%;background:var(--pink);margin-top:-40px}

  .flavor{position:absolute;left:207px;top:125px;display:flex;flex-direction:column;align-items:flex-start;gap:4px}
  .flavor span{background:var(--pink);color:var(--flavor-text);font:800 25px/1 "Rubik",sans-serif;padding:2px 7px 1px;letter-spacing:.5px}
  .label--lavender .flavor span{font-size:19.5px}

  .sku{position:absolute;left:207px;top:199px;font:400 10px/13px "Noto Serif",serif;color:var(--sku-grey)}
  .count{position:absolute;left:395px;top:138px;width:86px;text-align:center;color:var(--ink)}
  .count__num{font:700 54px/1 "Playfair Display",serif;color:var(--pink)}
  .count__text{font:400 10.5px/13px "Noto Serif",serif;margin-top:0}

  .panel{position:absolute;background:#fff;border:1.3px solid var(--ink);border-radius:18px;font-family:"Source Sans 3",sans-serif;color:var(--ink)}
  .panel--ingredients{left:30px;top:704px;width:496px;height:229px}
  .panel--compliance{left:678px;top:697px;width:496px;height:229px}

  .ingredients{position:absolute;left:23px;top:20px;width:410px;font:400 11px/15px "Source Sans 3",sans-serif}
  .ingredients b{font-weight:700}
  .facts{position:absolute;left:0;right:0;top:86px;text-align:center}
  .facts__title{display:inline-block;border:1.5px solid var(--ink);padding:0 6px;font:600 13px/17px "Source Sans 3",sans-serif}
  .facts__body{margin-top:6px;font:600 11px/15px "Source Sans 3",sans-serif}
  .site{position:absolute;left:0;right:0;top:164px;text-align:center;font:600 17px/1 "Source Sans 3",sans-serif}
  .storage{position:absolute;left:0;right:0;top:188px;text-align:center;font:400 17px/1 "Source Sans 3",sans-serif}

  .compliance{position:absolute;left:74px;top:23px;width:410px;font:400 15px/20.3px "Source Sans 3",sans-serif}
</style>
</head>
<body>
<main class="sheet">

  <section class="label label--lemon">
    <div class="label__frame"></div>
    <div class="peel-tab"><svg width="26" height="20" viewBox="0 0 26 20"><path d="M24 18 C22 8 14 5 7 8" fill="none" stroke="#fff" stroke-width="4"/><path d="M2 10 L10 2 L11 13 Z" fill="#fff"/></svg></div>
    <svg class="thc-icon" width="112" height="112" viewBox="0 0 112 112" aria-label="THC warning symbol">
      <path d="M56 2 L110 56 L56 110 L2 56 Z" fill="#fff"/>
      <path d="M56 12 L100 56 L56 100 L12 56 Z" fill="#fff" stroke="var(--warn-red)" stroke-width="4"/>
      <rect x="53" y="22" width="6" height="20" fill="var(--warn-red)"/><circle cx="56" cy="47" r="3.5" fill="var(--warn-red)"/>
      <text x="56" y="68" text-anchor="middle" font-family="Source Sans 3, sans-serif" font-weight="700" font-size="21" fill="var(--warn-red)">THC</text>
    </svg>
    <p class="warning">CONTAINS MARIJUANA.<br>KEEP AWAY<br>FROM CHILDREN</p>
    <div class="divider"></div>
    <div class="brand"><div class="brand__line">Chewables by</div><div class="brand__name"><span class="brand__word">norma</span><span class="brand__dot"></span></div></div>
    <div class="flavor"><span>LEMON</span><span>CHIFFON</span></div>
    <p class="sku">SKU specific details: Ginger,<br>3 mg THC, 10 mg CBD, 3 mg CBG.</p>
    <div class="count"><div class="count__num">30</div><div class="count__text">fast acting<br>chewable tablets</div></div>
  </section>

  <section class="label label--ginger">
    <div class="label__frame"></div>
    <div class="peel-tab"><svg width="26" height="20" viewBox="0 0 26 20"><path d="M24 18 C22 8 14 5 7 8" fill="none" stroke="#fff" stroke-width="4"/><path d="M2 10 L10 2 L11 13 Z" fill="#fff"/></svg></div>
    <svg class="thc-icon" width="112" height="112" viewBox="0 0 112 112" aria-label="THC warning symbol">
      <path d="M56 2 L110 56 L56 110 L2 56 Z" fill="#fff"/>
      <path d="M56 12 L100 56 L56 100 L12 56 Z" fill="#fff" stroke="var(--warn-red)" stroke-width="4"/>
      <rect x="53" y="22" width="6" height="20" fill="var(--warn-red)"/><circle cx="56" cy="47" r="3.5" fill="var(--warn-red)"/>
      <text x="56" y="68" text-anchor="middle" font-family="Source Sans 3, sans-serif" font-weight="700" font-size="21" fill="var(--warn-red)">THC</text>
    </svg>
    <p class="warning">CONTAINS MARIJUANA.<br>KEEP AWAY<br>FROM CHILDREN</p>
    <div class="divider"></div>
    <div class="brand"><div class="brand__line">Chewables by</div><div class="brand__name"><span class="brand__word">norma</span><span class="brand__dot"></span></div></div>
    <div class="flavor"><span>GINGER</span></div>
    <p class="sku">SKU specific details: Ginger,<br>3 mg THC, 10 mg CBD, 3 mg CBG.</p>
    <div class="count"><div class="count__num">30</div><div class="count__text">fast acting<br>chewable tablets</div></div>
  </section>

  <section class="label label--lavender">
    <div class="label__frame"></div>
    <div class="peel-tab"><svg width="26" height="20" viewBox="0 0 26 20"><path d="M24 18 C22 8 14 5 7 8" fill="none" stroke="#fff" stroke-width="4"/><path d="M2 10 L10 2 L11 13 Z" fill="#fff"/></svg></div>
    <svg class="thc-icon" width="112" height="112" viewBox="0 0 112 112" aria-label="THC warning symbol">
      <path d="M56 2 L110 56 L56 110 L2 56 Z" fill="#fff"/>
      <path d="M56 12 L100 56 L56 100 L12 56 Z" fill="#fff" stroke="var(--warn-red)" stroke-width="4"/>
      <rect x="53" y="22" width="6" height="20" fill="var(--warn-red)"/><circle cx="56" cy="47" r="3.5" fill="var(--warn-red)"/>
      <text x="56" y="68" text-anchor="middle" font-family="Source Sans 3, sans-serif" font-weight="700" font-size="21" fill="var(--warn-red)">THC</text>
    </svg>
    <p class="warning">CONTAINS MARIJUANA.<br>KEEP AWAY<br>FROM CHILDREN</p>
    <div class="divider"></div>
    <div class="brand"><div class="brand__line">Chewables by</div><div class="brand__name"><span class="brand__word">norma</span><span class="brand__dot"></span></div></div>
    <div class="flavor"><span>LAVENDER</span><span>POMEGRANATE</span></div>
    <p class="sku">SKU specific details: Ginger,<br>3 mg THC, 10 mg CBD, 3 mg CBG.</p>
    <div class="count"><div class="count__num">30</div><div class="count__text">fast acting<br>chewable tablets</div></div>
  </section>

  <section class="label label--matcha">
    <div class="label__frame"></div>
    <div class="peel-tab"><svg width="26" height="20" viewBox="0 0 26 20"><path d="M24 18 C22 8 14 5 7 8" fill="none" stroke="#fff" stroke-width="4"/><path d="M2 10 L10 2 L11 13 Z" fill="#fff"/></svg></div>
    <svg class="thc-icon" width="112" height="112" viewBox="0 0 112 112" aria-label="THC warning symbol">
      <path d="M56 2 L110 56 L56 110 L2 56 Z" fill="#fff"/>
      <path d="M56 12 L100 56 L56 100 L12 56 Z" fill="#fff" stroke="var(--warn-red)" stroke-width="4"/>
      <rect x="53" y="22" width="6" height="20" fill="var(--warn-red)"/><circle cx="56" cy="47" r="3.5" fill="var(--warn-red)"/>
      <text x="56" y="68" text-anchor="middle" font-family="Source Sans 3, sans-serif" font-weight="700" font-size="21" fill="var(--warn-red)">THC</text>
    </svg>
    <p class="warning">CONTAINS MARIJUANA.<br>KEEP AWAY<br>FROM CHILDREN</p>
    <div class="divider"></div>
    <div class="brand"><div class="brand__line">Chewables by</div><div class="brand__name"><span class="brand__word">norma</span><span class="brand__dot"></span></div></div>
    <div class="flavor"><span>MATCHA</span><span>PEPPERMINT</span></div>
    <p class="sku">SKU specific details: Ginger,<br>3 mg THC, 10 mg CBD, 3 mg CBG.</p>
    <div class="count"><div class="count__num">30</div><div class="count__text">fast acting<br>chewable tablets</div></div>
  </section>

  <section class="panel panel--ingredients">
    <p class="ingredients"><b>INGREDIENTS:</b> GINGER, SUGAR, MALTODEXTRIN, MAGNESIUM STEARATE, MICROCRYSTALLINE CELLULOSE, DICALCIUM PHOSPHATE, SILICON DIOXIDE, AND FOOD GRADE COLORANT, HEMP DERIVED CBD AND CBG, MARIJUANA DERIVED THC.</p>
    <div class="facts">
      <div class="facts__title">PLEASE HAVE A PRODUCT FACTS BOX CONTAINING THIS:</div>
      <p class="facts__body">SERVING SIZE 1 TABLET = 3 MG THC, 10 MG CBD, 3 MG CBG<br>TOTAL CANNABINOIDS PER PACKAGE 90 MG THC, 300 MG CBD, 90 MG CBG.<br>480 MG TOTAL CANNABINOIDS. TOTAL NET WEIGHT: 10.5 G</p>
    </div>
    <p class="site">WWW.NORMAVELTA.COM</p>
    <p class="storage">STORE IN A COOL DRY PLACE</p>
  </section>

  <section class="panel panel--compliance">
    <p class="compliance">THIS PRODUCT WAS PRODUCED WITHOUT REGULATORY OVERSIGHT FOR HEALTH, SAFETY, OR EFFICACY. THERE MAY BE LONG TERM PHYSICAL OR MENTAL HEALTH RISKS FOR USE OF MARIJUANA INCLUDING ADDITIONAL RISKS FOR WOMEN WHO ARE OR MAY BE PREGNANT OR ARE BREASTFEEDING. USE OF MARIJUANA MAY IMPAIR YOUR ABILITY TO DRIVE A CAR OR OPERATE MACHINERY.<br>THE INTOXICATING EFFECTS OF THIS PRODUCT MAY BE DELAYED BY UP TO 4 HOURS.</p>
  </section>

</main>
</body>
</html>
```